Wine Bottle Label for Tall Fern Cellars

We are a small, newly established winery in need of an original, bold and outstanding bottle label design for our Tall Fern wine.

Our vineyard and winery are located on a 200 acre farm in a remote part of southern Oregon. The name "Tall Fern" was inspired by the large, overgrown size of all of the foliage here, including our grapevines. Things grow large and vigorous in Oregon! And everything is very lush and green. It is almost surreal or other-worldly, like the landscapes seen in the Keeper of The Hollows movies, or the land of Yarrowmere. It is a place that makes you say "wow" with its epic, large scale, natural beauty.

The name "Tall Fern" also captures the essence of our wine. It is big in flavor, quality and color. Our first release is a Pinot Noir (red). Pinot Noir wines often are subtle in flavor and thin in their color. Our label should convey that our Pinot Noir is a much more robust, darker, heavier, meatier, more flavorful wine that is a lot more fun than an "ordinary" wine. At the same time, this wine is not cheap, and so nothing in the label should convey "bargain," "low price," or "cheapness." This is a fine wine with a sense of adventure. Be sure to convey "quality" with your design along with "big," "adventure" and "fun".

The label should appeal to a younger demographic, both male and female, between the ages of 21 and 35. It should be non-traditional and adventurous and suggest a pushing of boundaries and a breaking of rules. This Pinot Noir does not conform to the normal "limitations" of the variety, therefore the label should not conform. It should have an "organic" or "natural" or "agricultural" vibe, as opposed to something mechanical or technical. It should, however, be contemporary. Do not confuse "natural" or "organic" with being nostalgic or old school. Think "agri-hipsters."

The label should be designed to fit on a Burgundy-style wine bottle (photo attached for reference). (Note: All Pinot Noir and Chardonnay is bottled in Burgundy bottles, If you are not sure about the bottle shape you can go to a local store and compare the various bottles. Locate a bottle of Pinot Noir or Chardonnay or anything identified as a "Burgundy Wine," and it should be the correct bottle. The tall, skinny bottles used for Cabernet Sauvignon are NOT correct)). Please see the "Must Have" notes for more on the bottle.

In summary, the final project should be a wine bottle label design that conveys bigness, vastness, adventurous, non-traditional, high quality wine. A good tagline to keep in mind is "Living Large."

Target Market(s)

Young, hip, non-conformist wine drinkers aged 21-35 with a sense of adventure and an appreciation of quality.

Industry/Entity Type

School

Requirements
Must have
• *Must contain the words:

Tall Fern (the brand)
2013 Pinot Noir (the vintage year and variety)

*The label must be designed to fit a Burgundy-style wine bottle. A photo is attached for reference.

*Additionally, the label needs to fit on the lower, widest part of the bottle. The label will be printed on sticky paper and rolled onto the bottle with a machine. The machine cannot apply labels to the neck of the bottle. The maximum size of a label that will fit this space is 5.5 inches wide by 4.5 inches tall. You DO NOT have to fill ALL of this space or confine the label shape to a rectangle, but the label cannot exceed this size or it won't stick to the bottle properly. It will really help if you can put your hands on an actual bottle to see the logistics of applying the label. But if that is not possible, just do your best with the instructions you have. I am confident the winning design could be adjusted to fit the bottle, if necessary
Nice to have
• *Wine grape leaf or leaves.

*A concept I have been playing with is sunlight shining through leaves like light through a Kessler lamp or a stained glass window. This is NOT a requirement for this label. However, if the concept inspires and idea, I would be most happy to see it.
Should not have
• IF a leaf or leaves are included in the design (not a requirement) they MUST be wine grapevine leafs and preferably leaves of the Pinot Noir vine. Do not use generic leaves or identifiable leaves such as oak leaves, maple leaves, or anything that looks like the Canadian flag or the Dunmore Ice Hawks hockey logo. Reference the attached photos of wine grape leaves to see the correct leaf type. I am happy to email more photos upon request. These photos may be used in whole or in part in your design, however, a leaf from a photo is NOT a requirement, nor is the image of a leaf or leaves.

This label should NOT be designed for Bordeaux-style wine bottles (the tall, skinny ones).

```html
<!DOCTYPE html>
<html lang="en">
<head>
<meta charset="utf-8">
<title>Tall Fern Cellars – 2013 Pinot Noir Label</title>
<link rel="stylesheet" href="https://fonts.googleapis.com/css2?family=Great+Vibes&family=Federant&family=Cinzel:wght@400&display=swap">
<style>
  :root {
    --border-coral: #e8553f;
    --olive: #8b7c2f;
    --leaf-deep: #2f8a3c;
    --leaf-mid: #5fa832;
    --leaf-light: #a9c83a;
    --badge-black: #0d0d0d;
    --badge-yellow: #e9e45a;
    --title-red: #e3191b;
    --ink: #111111;
  }
  html, body {
    margin: 0;
    padding: 0;
    width: 1200px;
    height: 624px;
    overflow: hidden;
    background: #ffffff;
  }
  .label {
    position: relative;
    width: 1200px;
    height: 624px;
    background: var(--border-coral);
    overflow: hidden;
  }
  .label__field {
    position: absolute;
    left: 24px;
    top: 0;
    width: 1153px;
    height: 602px;
    background: var(--olive);
  }
  .label__foliage {
    position: absolute;
    inset: 0;
    width: 1200px;
    height: 624px;
  }
  .vintage-badge {
    position: absolute;
    left: 533px;
    top: 55px;
    width: 138px;
    height: 138px;
    border-radius: 50%;
    background: var(--badge-black);
    display: flex;
    align-items: center;
    justify-content: center;
  }
  .vintage-badge__inner {
    width: 104px;
    height: 104px;
    border-radius: 50%;
    background: var(--badge-yellow);
    display: flex;
    align-items: center;
    justify-content: center;
    font-family: "Cinzel", serif;
    font-size: 34px;
    color: var(--ink);
    letter-spacing: 0;
  }
  .brand-name {
    position: absolute;
    left: 0;
    width: 1212px;
    top: 185px;
    margin: 0;
    text-align: center;
    font-family: "Great Vibes", cursive;
    font-weight: 400;
    font-size: 210px;
    line-height: 1;
    color: var(--title-red);
    -webkit-text-stroke: 3px var(--ink);
    paint-order: stroke fill;
  }
  .variety {
    position: absolute;
    left: 0;
    width: 1206px;
    top: 492px;
    margin: 0;
    text-align: center;
    font-family: "Federant", serif;
    font-size: 42px;
    line-height: 1;
    color: var(--ink);
  }
  .spec {
    position: absolute;
    top: 544px;
    font-family: "Federant", serif;
    font-size: 22px;
    line-height: 1;
    color: var(--ink);
  }
  .spec--volume { left: 86px; }
  .spec--abv { right: 90px; }
</style>
</head>
<body>
  <div class="label">
    <div class="label__field"></div>

    <svg class="label__foliage" viewBox="0 0 1200 624" role="img" aria-label="Close-up photograph of large green grapevine leaves with visible veins, torn edge along the lower right">
      <defs>
        <linearGradient id="foliageTone" x1="0" y1="0" x2="1" y2="0.6">
          <stop offset="0" stop-color="var(--leaf-deep)"/>
          <stop offset="0.45" stop-color="var(--leaf-mid)"/>
          <stop offset="1" stop-color="var(--leaf-light)"/>
        </linearGradient>
      </defs>
      <polygon fill="url(#foliageTone)" points="0,0 1138,0 1138,33 1098,89 1049,114 1000,130 971,163 919,195 813,220 732,244 642,260 561,293 504,301 455,350 423,407 407,455 415,488 390,528 358,537 309,504 244,480 163,472 81,463 24,455 0,455"/>
    </svg>

    <div class="vintage-badge">
      <div class="vintage-badge__inner">2013</div>
    </div>

    <h1 class="brand-name">Tall Fern</h1>
    <p class="variety">Pinot Noir</p>
    <span class="spec spec--volume">..CL</span>
    <span class="spec spec--abv">..%Vol</span>
  </div>
</body>
</html>
```